Oil and Gas Exploration and Production company needs a business card design

We need a business card design using our logo and colors in the logo. We want a mainstream design.

```html
<!DOCTYPE html>
<html lang="en">
<head>
<meta charset="utf-8">
<title>Tarn Oil &amp; Gas – Business Card</title>
<link rel="stylesheet" href="https://fonts.googleapis.com/css2?family=Lato:wght@400;700;900&display=swap">
<style>
  :root {
    --page-bg: #ffffff;
    --card-bg: #ffffff;
    --ink: #111111;
    --body-grey: #555555;
    --gold: #c8952a;
    --card-edge: #e6e6e6;
  }
  html, body {
    margin: 0;
    padding: 0;
    width: 1200px;
    height: 1200px;
    overflow: hidden;
    background: var(--page-bg);
    font-family: "Lato", Arial, sans-serif;
  }
  .canvas {
    position: relative;
    width: 1200px;
    height: 1200px;
  }
  .business-card {
    position: absolute;
    left: 246px;
    top: 398px;
    width: 708px;
    height: 404px;
    background: var(--card-bg);
    border: 1px solid var(--card-edge);
    box-sizing: border-box;
  }
  .holder-name {
    position: absolute;
    left: 38px;
    top: 40px;
    margin: 0;
    font-size: 28px;
    font-weight: 700;
    color: var(--ink);
    letter-spacing: -0.2px;
  }
  .holder-title {
    position: absolute;
    left: 39px;
    top: 76px;
    margin: 0;
    font-size: 16px;
    font-weight: 700;
    color: var(--gold);
  }
  .address {
    position: absolute;
    left: 40px;
    top: 175px;
    margin: 0;
    font-style: normal;
    font-size: 16px;
    line-height: 24px;
    color: var(--body-grey);
  }
  .contact-list {
    position: absolute;
    left: 40px;
    top: 296px;
    margin: 0;
    padding: 0;
    list-style: none;
    font-size: 16px;
    color: var(--body-grey);
  }
  .contact-list li {
    display: flex;
    align-items: center;
    height: 25px;
  }
  .contact-icon {
    width: 12px;
    height: 12px;
    margin-right: 10px;
    fill: var(--gold);
    flex: none;
  }
  .web-accent { color: var(--gold); }
  .brand {
    position: absolute;
    right: 42px;
    bottom: 58px;
    display: flex;
    align-items: center;
  }
  .brand-dot {
    width: 40px;
    height: 40px;
    border-radius: 50%;
    background: var(--gold);
    margin-right: 12px;
  }
  .brand-name {
    font-size: 36px;
    font-weight: 900;
    color: var(--ink);
    letter-spacing: 0.2px;
    white-space: nowrap;
  }
</style>
</head>
<body>
<main class="canvas">
  <section class="business-card" aria-label="Business card">
    <h1 class="holder-name">Daniel Hart</h1>
    <p class="holder-title">President</p>

    <address class="address">
      Unit 4/58 Harbour Rd<br>
      Port Kelby SA 5611
    </address>

    <ul class="contact-list">
      <li>
        <svg class="contact-icon" viewBox="0 0 24 24" aria-hidden="true">
          <path d="M6.6 10.8a15.1 15.1 0 0 0 6.6 6.6l2.2-2.2a1 1 0 0 1 1-.25 11.4 11.4 0 0 0 3.6.57 1 1 0 0 1 1 1V20a1 1 0 0 1-1 1A17 17 0 0 1 3 4a1 1 0 0 1 1-1h3.5a1 1 0 0 1 1 1c0 1.25.2 2.45.57 3.6a1 1 0 0 1-.25 1z"/>
        </svg>
        (08) 8120 4417
      </li>
      <li>
        <svg class="contact-icon" viewBox="0 0 24 24" aria-hidden="true">
          <path d="M2 5h20v14H2z M2 5l10 8 10-8" fill="var(--gold)"/>
          <path d="M3 6l9 7 9-7" fill="none" stroke="#fff" stroke-width="1.8"/>
        </svg>
        hello@tarnoil.com
      </li>
      <li>
        <svg class="contact-icon" viewBox="0 0 24 24" aria-hidden="true">
          <circle cx="12" cy="12" r="10"/>
          <path d="M2 12h20M12 2c3 3 3 17 0 20M12 2c-3 3-3 17 0 20M4 7h16M4 17h16" fill="none" stroke="#fff" stroke-width="1.4"/>
        </svg>
        <span>www.<span class="web-accent">tarnoil</span>.com</span>
      </li>
    </ul>

    <div class="brand">
      <span class="brand-dot" aria-hidden="true"></span>
      <span class="brand-name">Tarn Oil &amp; Gas</span>
    </div>
  </section>
</main>
</body>
</html>
```